Rewards Card Design Project

We require a rewards card design for an Indian cuisine restaurant. We wish to keep the design somewhat simple and also professional. We have uploaded the relevant artwork and you may use any of it in the design. The design should include restaurant logo, phone number, address and website address and should include words "rewards card". (The restaurant details are included in the uploaded files). Also we wish the design to be in a format suitable for printing e.g. Adobe Air, CorelDraw etc

Thank you for sending your designs. We've really liked few of them but will wait until end of this week before making final selection. We wish to inform that all designs should be in landscape mode. We intend to print it on cards which are equal in size to standard credit cards (85.60 mm × 53.98 mm). Please also consider the bleeding area while making the designs.

Industry/Entity Type

Restaurant

```html
<!DOCTYPE html>
<html lang="en">
<head>
<meta charset="utf-8">
<title>Saffron Vale – Rewards Card</title>
<link rel="stylesheet" href="https://fonts.googleapis.com/css2?family=Open+Sans:wght@600;700&family=Cinzel:wght@700&family=Dancing+Script:wght@400&display=swap">
<style>
  :root {
    --page: #ffffff;
    --card: #353334;
    --wood-dark: #3a2418;
    --wood: #7a4a2c;
    --gold: #d2a865;
    --ink: #1b1a1a;
    --band: #221f20;
    --white: #ffffff;
    --caption: #333333;
    --curry: #b0552a;
    --curry-deep: #7a3418;
    --plate: #e9e6e1;
  }
  html, body {
    margin: 0;
    width: 1200px;
    height: 1000px;
    overflow: hidden;
    background: var(--page);
  }
  .canvas { position: relative; width: 1200px; height: 1000px; }

  .reward-card {
    position: absolute;
    left: 95px; top: 130px;
    width: 1010px; height: 637px;
    overflow: hidden;
    background: linear-gradient(90deg, var(--card) 0%, var(--card) 55%, var(--wood-dark) 78%, var(--wood) 100%);
  }

  .dish-photo {
    position: absolute;
    left: 500px; top: 80px;
    width: 560px; height: 520px;
    border-radius: 50%;
    background:
      radial-gradient(ellipse 48% 45% at 62% 48%, #d46a34 0%, var(--curry) 40%, var(--curry-deep) 72%, transparent 74%),
      radial-gradient(ellipse 58% 52% at 60% 48%, var(--plate) 0%, #cfcac3 70%, transparent 72%);
    -webkit-mask-image: linear-gradient(90deg, transparent 0%, #000 30%);
            mask-image: linear-gradient(90deg, transparent 0%, #000 30%);
  }

  .border-pattern {
    position: absolute;
    left: 0; width: 1010px; height: 26px;
    background: linear-gradient(180deg, transparent 0 30%, var(--gold) 30% 70%, transparent 70%);
    opacity: 0.85;
  }
  .border-pattern--top { top: 32px; }
  .border-pattern--bottom { top: 578px; }

  .brand-plate {
    position: absolute;
    left: 79px; top: 96px;
    width: 632px; height: 111px;
    background: var(--gold);
    display: flex; align-items: center; justify-content: center;
    font-family: "Open Sans", sans-serif;
    font-weight: 700;
    font-size: 64px;
    color: var(--ink);
    letter-spacing: 1px;
  }
  .brand-tagline {
    position: absolute;
    left: 79px; top: 207px;
    width: 632px; height: 67px;
    background: var(--band);
    display: flex; align-items: center; justify-content: center;
    font-family: "Cinzel", serif;
    font-weight: 700;
    font-size: 40px;
    color: var(--white);
    letter-spacing: 2px;
  }

  .card-title {
    position: absolute;
    left: 80px; top: 290px;
    margin: 0;
    font-family: "Dancing Script", cursive;
    font-weight: 400;
    font-size: 76px;
    color: var(--white);
  }

  .contact {
    position: absolute;
    left: 79px; top: 430px;
    font-family: "Open Sans", sans-serif;
    font-weight: 700;
    color: var(--white);
  }
  .contact p { margin: 0; }
  .contact .website { font-size: 25px; line-height: 34px; margin-bottom: 8px; }
  .contact .line { font-size: 22px; line-height: 40px; }

  .size-caption {
    position: absolute;
    left: 0; top: 833px; width: 1200px;
    text-align: center;
    font-family: Arial, Helvetica, sans-serif;
    font-size: 36px;
    color: var(--caption);
  }
</style>
</head>
<body>
<div class="canvas">
  <section class="reward-card">
    <div class="dish-photo" role="img" aria-label="Photo of a prawn curry on a white plate, garnished with spring onion and tomato"></div>
    <div class="border-pattern border-pattern--top" role="img" aria-label="Gold repeating ornamental border"></div>
    <div class="border-pattern border-pattern--bottom" role="img" aria-label="Gold repeating ornamental border"></div>

    <div class="brand-plate">Saffron Vale</div>
    <div class="brand-tagline">INDIAN RESTAURANT</div>

    <h1 class="card-title">Rewards Card</h1>

    <div class="contact">
      <p class="website">www.SaffronVale.com.au</p>
      <p class="line">Dine In • Take-Away • Home Delivery</p>
      <p class="line">Ph. 9000 4821 • 18 Linden Street, Ashby</p>
    </div>
  </section>

  <div class="size-caption">85.6 x 53.98 mm</div>
</div>
</body>
</html>
```